Simple, Professional and neat business card design for Vellamor Inc.

We're looking to re-vamp our business card design. We're a supplier of innovative feed ingredients for the North American animal agriculture industry. We are located in Lucknow, Ontario, Canada and our flagship product is a product that prevents milk fever in dairy cows when the calve, it is fed before calving and is very effective compared to other alternatives available on the market today.

Our company has Danish roots and we import all of our product from our Danish partner/manufacturer in Denmark. We like our design to embrace high professionalism while remaining neat and simple.

Target Market(s)

B2B, Feed Mills, Veterinary Clinics, Large integrators/producers,

Industry/Entity Type

Agribusiness

Contact Information for Business Card

We like the rounded corners because they make the card easy to sit in a wallet and not many use it so it makes the card stand out, just possibly something to take account for during the design.

As you can also see on the sliders below, looking for a that simple but proffesional scandinavian design.

Requirements
Nice to have
• Rounded corners
Should not have
• Too vibrant

```html
<!DOCTYPE html>
<html lang="en">
<head>
<meta charset="utf-8">
<title>Vellamor Inc. — Business Card</title>
<link rel="stylesheet" href="https://fonts.googleapis.com/css2?family=Open+Sans:wght@400;600;700;800&display=swap">
<style>
  :root {
    --stage: #1c1c1e;
    --brand-blue: #0d4f97;
    --brand-blue-deep: #08305f;
    --brand-blue-light: #1f6cc0;
    --card-paper: #ededed;
    --ink: #3a3a3a;
    --rule: #cfcfcf;
    --muted-dot: #9a9ea6;
    --white: #ffffff;
  }
  * { box-sizing: border-box; margin: 0; padding: 0; }
  html, body {
    width: 1200px; height: 900px; overflow: hidden;
    background: var(--stage);
    font-family: "Open Sans", Arial, sans-serif;
  }
  .stage {
    width: 1200px; height: 900px;
    display: flex; flex-direction: column; align-items: center; justify-content: center;
    gap: 60px;
  }
  .card {
    width: 560px; height: 320px;
    border-radius: 28px;
    position: relative; overflow: hidden;
  }

  /* Front */
  .card--front {
    background: radial-gradient(ellipse at 50% 40%, var(--brand-blue-light) 0%, var(--brand-blue) 45%, var(--brand-blue-deep) 100%);
    color: var(--white);
  }
  .front-mark {
    position: absolute; left: 0; right: 0; top: 110px;
    display: flex; align-items: center; justify-content: center; gap: 14px;
  }
  .front-mark__dot { width: 22px; height: 22px; border-radius: 50%; background: var(--white); }
  .front-mark__name { font-weight: 700; font-size: 34px; letter-spacing: 1px; color: var(--white); }
  .tagline {
    position: absolute; left: 0; right: 0; bottom: 34px;
    text-align: center; font-weight: 600; font-size: 15px; letter-spacing: 0.6px;
  }

  /* Back */
  .card--back { background: var(--card-paper); color: var(--ink); }
  .back-mark {
    position: absolute; left: 0; right: 0; top: 40px;
    display: flex; align-items: center; justify-content: center; gap: 12px;
  }
  .back-mark__dot { width: 26px; height: 26px; border-radius: 50%; background: var(--brand-blue); }
  .back-mark__name { font-weight: 800; font-size: 30px; color: var(--brand-blue); letter-spacing: 0.5px; }
  .divider {
    position: absolute; left: 40px; right: 40px; top: 104px;
    border-top: 1px solid var(--rule);
  }
  .company-contacts {
    position: absolute; right: 40px; top: 118px;
    text-align: right; font-size: 15px; line-height: 22px;
  }
  .company-contacts li, .person-contacts li { list-style: none; display: flex; align-items: center; gap: 6px; }
  .company-contacts li { justify-content: flex-end; }
  .icon { width: 12px; height: 12px; fill: var(--brand-blue); flex: none; }
  .social-row { display: flex; justify-content: flex-end; gap: 5px; margin-top: 6px; }
  .social-row span { width: 20px; height: 20px; border-radius: 50%; background: var(--muted-dot); }
  .person {
    position: absolute; left: 40px; bottom: 30px;
  }
  .person__name {
    font-weight: 600; font-size: 19px; color: var(--brand-blue); letter-spacing: 0.4px;
    padding-bottom: 6px; margin-bottom: 8px; border-bottom: 1px solid var(--rule); width: 200px;
  }
  .person-contacts { font-size: 15px; line-height: 20px; }
  .toll-free { color: var(--brand-blue); }
  .address { font-size: 15px; line-height: 20px; margin-top: 2px; }
</style>
</head>
<body>
<main class="stage">
  <section class="card card--front" aria-label="Card front">
    <div class="front-mark">
      <span class="front-mark__dot"></span>
      <span class="front-mark__name">VELLAMOR INC.</span>
    </div>
    <p class="tagline">PROTECTING THE HEALTH OF YOUR ANIMALS</p>
  </section>

  <section class="card card--back" aria-label="Card back">
    <div class="back-mark">
      <span class="back-mark__dot"></span>
      <span class="back-mark__name">VELLAMOR INC.</span>
    </div>
    <div class="divider"></div>

    <ul class="company-contacts">
      <li>519-555-0142
        <svg class="icon" viewBox="0 0 12 12"><rect x="2" y="0" width="8" height="4"/><rect x="0" y="4" width="12" height="5" rx="1"/><rect x="2" y="8" width="8" height="4"/></svg>
      </li>
      <li>mikkel@vellamor.com
        <svg class="icon" viewBox="0 0 12 12"><rect x="0" y="2" width="12" height="8" rx="1"/><path d="M0 2 L6 7 L12 2" stroke="#fff" stroke-width="1" fill="none"/></svg>
      </li>
      <li>www.vellamor.com
        <svg class="icon" viewBox="0 0 12 12"><circle cx="6" cy="6" r="6"/><path d="M0 6h12M6 0c-3 3-3 9 0 12M6 0c3 3 3 9 0 12" stroke="#fff" stroke-width="0.8" fill="none"/></svg>
      </li>
      <li class="social-row"><span></span><span></span><span></span><span></span><span></span></li>
    </ul>

    <div class="person">
      <h2 class="person__name">MIKKEL DAHLGAARD</h2>
      <ul class="person-contacts">
        <li><svg class="icon" viewBox="0 0 12 12"><rect x="2" y="0" width="8" height="12" rx="1.5"/><rect x="3.5" y="1.5" width="5" height="7" fill="#fff"/></svg>519-555-0187</li>
        <li><svg class="icon" viewBox="0 0 12 12"><path d="M0 4c0-2 2-3 6-3s6 1 6 3v1H9V3.5H3V5H0z"/><rect x="2" y="6" width="8" height="5" rx="1"/></svg>519-555-0163</li>
        <li><svg class="icon" viewBox="0 0 12 12"><path d="M0 4c0-2 2-3 6-3s6 1 6 3v1H9V3.5H3V5H0z"/><rect x="2" y="6" width="8" height="5" rx="1"/></svg>888-555-0119<span class="toll-free">(TOLL FREE)</span></li>
      </ul>
      <p class="address">Box 412, Elmbrook Valley<br>Canada X9X 4B2</p>
    </div>
  </section>
</main>
</body>
</html>
```